Hal's Remedies Business Card Design Project

I need a business card designed for my pharmacy Hal's Remedies. I would like just the logo on one side, maybe with black background and white lettering. The other side I would also like to include my logo which is attached. Also, please include my name and the following information:
Hal Norwick Owner/Pharm D.
Business address is 7163 N Birch Rd Alder Falls, ND 57291.
Phone number is 605-318-6027 and fax # is 605-318-6031.
my email address is hal@halsremedies.example.
My website is www.halsremedies.example.
My business hours are Monday-Friday 9am-6 pm. Saturday 9am-1 pm. Sunday Closed.
I would like the design to include my logo colors, black, white, and neon green. Silver may be added as a highlight. Thanks.
Pharmacy
See above in product description

```html
<!DOCTYPE html>
<html lang="en">
<head>
<meta charset="utf-8">
<title>Hal's Remedies – Business Card</title>
<link rel="stylesheet" href="https://fonts.googleapis.com/css2?family=Open+Sans:wght@600&family=Arimo:wght@400;700&display=swap">
<style>
  :root {
    --page-bg: #e6e6e6;
    --card-white: #ffffff;
    --card-light: #ececec;
    --ink-dark: #3a3a3a;
    --panel-black: #0f0f0f;
    --silver-light: #d9d9d9;
    --silver-dark: #7a7a7a;
    --strip-grey: #4a4a4a;
    --strip-text: #c9c9c9;
    --text-white: #ffffff;
    --accent-green: #8dc63f;
    --accent-orange: #f08a3c;
    --rule-grey: #8a8a8a;
  }
  html, body {
    margin: 0;
    width: 1200px;
    height: 900px;
    overflow: hidden;
    background: var(--page-bg);
  }
  .canvas {
    position: relative;
    width: 1200px;
    height: 900px;
  }
  .card {
    position: absolute;
    left: 250px;
    width: 700px;
    height: 400px;
    overflow: hidden;
    box-shadow: 0 6px 18px rgba(0,0,0,0.18);
  }
  .card--front { top: 30px; background: var(--card-white); }
  .card--back {
    top: 470px;
    background: radial-gradient(ellipse at 55% 40%, var(--card-white) 0%, var(--card-light) 100%);
  }
  .front-shapes {
    position: absolute;
    inset: 0;
  }
  .brand {
    position: absolute;
    display: flex;
    align-items: center;
  }
  .brand__dot {
    width: 34px;
    height: 34px;
    border-radius: 50%;
    background: var(--accent-green);
  }
  .brand__rule {
    width: 1px;
    height: 64px;
    background: var(--ink-dark);
    margin: 0 20px;
  }
  .brand__name {
    font-family: "Open Sans", sans-serif;
    font-weight: 600;
    font-size: 54px;
    letter-spacing: -1.5px;
    color: var(--ink-dark);
    white-space: nowrap;
  }
  .card--front .brand { left: 36px; top: 36px; }
  .card--back .brand {
    left: 50%;
    top: 150px;
    transform: translateX(-50%);
  }
  .owner {
    position: absolute;
    left: 40px;
    top: 284px;
    font-family: "Arimo", sans-serif;
  }
  .owner__name {
    color: var(--text-white);
    font-size: 22px;
    letter-spacing: 0.5px;
  }
  .owner__title {
    color: var(--accent-orange);
    font-size: 18px;
    margin-top: 4px;
  }
  .divider {
    position: absolute;
    left: 312px;
    top: 250px;
    width: 1px;
    height: 92px;
    background: var(--rule-grey);
  }
  .contact {
    position: absolute;
    left: 336px;
    top: 194px;
    margin: 0;
    font-family: "Arimo", sans-serif;
    font-size: 16px;
    line-height: 26px;
    color: var(--text-white);
  }
  .contact dt {
    display: inline;
    font-weight: 700;
  }
  .contact dd {
    display: inline;
    margin: 0;
  }
  .contact div { margin: 0; }
  .hours {
    position: absolute;
    left: 0;
    right: 0;
    bottom: 0;
    margin: 0;
    height: 36px;
    line-height: 36px;
    padding-left: 40px;
    background: var(--strip-grey);
    color: var(--strip-text);
    font-family: "Arimo", sans-serif;
    font-size: 14px;
  }
  .website {
    position: absolute;
    left: 40px;
    bottom: 30px;
    margin: 0;
    font-family: "Arimo", sans-serif;
    font-size: 15px;
    color: var(--ink-dark);
  }
</style>
</head>
<body>
<main class="canvas">

  <section class="card card--front" aria-label="Business card front">
    <svg class="front-shapes" width="700" height="400" viewBox="0 0 700 400" aria-hidden="true">
      <defs>
        <linearGradient id="silver-band" x1="0" y1="0" x2="0" y2="1">
          <stop offset="0" stop-color="#d9d9d9"/>
          <stop offset="1" stop-color="#7a7a7a"/>
        </linearGradient>
        <linearGradient id="black-panel" x1="0" y1="0" x2="1" y2="1">
          <stop offset="0" stop-color="#2a2a2a"/>
          <stop offset="0.5" stop-color="#0f0f0f"/>
          <stop offset="1" stop-color="#000"/>
        </linearGradient>
      </defs>
      <path d="M0,212 C220,192 470,128 700,52 L700,76 C470,152 220,216 0,236 Z" fill="url(#silver-band)"/>
      <path d="M0,236 C220,216 470,152 700,76 L700,364 L0,364 Z" fill="url(#black-panel)"/>
    </svg>

    <div class="brand">
      <span class="brand__dot" aria-hidden="true"></span>
      <span class="brand__rule" aria-hidden="true"></span>
      <span class="brand__name">Hal's Remedies</span>
    </div>

    <div class="owner">
      <div class="owner__name">HAL NORWICK</div>
      <div class="owner__title">Owner/Pharm D</div>
    </div>

    <span class="divider" aria-hidden="true"></span>

    <dl class="contact">
      <div><dt>Address :</dt> <dd>7163 N Birch Rd Alder Falls<br>ND 57291.</dd></div>
      <div><dt>Phone :</dt> <dd>605-318-6027</dd></div>
      <div><dt>Fax :</dt> <dd>605-318-6031.</dd></div>
      <div><dt>Email :</dt> <dd>hal@halsremedies.example.</dd></div>
      <div><dt>Web :</dt> <dd>www.halsremedies.example.</dd></div>
    </dl>

    <p class="hours">My business hours are Monday-Friday 9am-6 pm. Saturday 9am-1 pm. Sunday Closed.</p>
  </section>

  <section class="card card--back" aria-label="Business card back">
    <div class="brand">
      <span class="brand__dot" aria-hidden="true"></span>
      <span class="brand__rule" aria-hidden="true"></span>
      <span class="brand__name">Hal's Remedies</span>
    </div>
    <p class="website">www.halsremedies.example</p>
  </section>

</main>
</body>
</html>
```